Korvane Sky Works, LLC - Business Card

I currently have a drone business that specializes in aerial photography, thermal image inspections, deer recovery, search and rescue, custom agricultural applications. i will attach my current business card as well as some logos to incorporate for a new up to date business card
Updates

Designs look the same

Sick

Target Market(s)

farmers, hunters

Contact Information for Business Card

name address phone number (as existing card i attached)

Requirements
Must have
• im good with existing business card, but would like an agricultural twist

```html
<!DOCTYPE html>
<html lang="en">
<head>
<meta charset="utf-8">
<title>Korvane Sky Works, LLC – Business Card</title>
<link rel="stylesheet" href="https://fonts.googleapis.com/css2?family=Oswald:wght@500;600&family=Poppins:wght@400;500&display=swap">
<style>
  :root {
    --bg: #2a2a2c;
    --card-white: #ffffff;
    --card-black: #1b1c1e;
    --green: #4a9a1f;
    --green-dark: #2f7a14;
    --ink: #1e1e1e;
    --rule: #9a9a9a;
    --white: #ffffff;
  }
  * { margin: 0; padding: 0; box-sizing: border-box; }
  html, body { width: 1200px; height: 1108px; overflow: hidden; }
  body {
    background: var(--bg);
    position: relative;
    font-family: "Poppins", sans-serif;
  }
  .card {
    position: absolute;
    top: 169px;
    width: 440px;
    height: 770px;
    border-radius: 26px;
    overflow: hidden;
  }
  .card-front { left: 120px; background: var(--card-white); color: var(--ink); text-align: center; }
  .card-back { left: 640px; background: var(--card-black); color: var(--white); }

  /* front */
  .brand-block {
    position: absolute; top: 120px; left: 0; right: 0;
    display: flex; align-items: center; justify-content: center; gap: 14px;
  }
  .brand-dot { width: 26px; height: 26px; border-radius: 50%; background: var(--green); }
  .brand-name {
    font-family: "Oswald", sans-serif; font-weight: 600;
    font-size: 46px; color: var(--green); letter-spacing: 1px; text-transform: uppercase;
  }
  .person-name {
    position: absolute; top: 372px; left: 0; right: 0;
    font-family: "Oswald", sans-serif; font-weight: 600;
    font-size: 44px; color: var(--green); letter-spacing: -1px; text-transform: uppercase;
  }
  .person-role { position: absolute; top: 430px; left: 0; right: 0; font-size: 21px; }
  .icon-row {
    position: absolute; top: 470px; left: 40px; right: 40px;
    display: flex; align-items: center; gap: 8px;
  }
  .icon-row .rule { flex: 1; height: 1px; background: var(--rule); }
  .icon-box {
    width: 38px; height: 38px; border-radius: 5px; background: var(--green);
    display: flex; align-items: center; justify-content: center;
  }
  .contact-list { position: absolute; top: 528px; left: 0; right: 0; font-size: 21px; line-height: 34px; }
  .contact-list .web-accent { color: var(--green); }
  .divider { position: absolute; top: 644px; left: 60px; right: 60px; height: 1px; background: var(--rule); }
  .address { position: absolute; top: 662px; left: 0; right: 0; font-size: 20px; line-height: 30px; }

  /* back */
  .pattern-field {
    position: absolute; inset: 0 0 230px 0;
    background: linear-gradient(160deg, #2a2b2e 0%, #1f2022 55%, #1b1c1e 100%);
  }
  .back-mark {
    position: absolute; top: 470px; right: 56px;
    font-family: "Oswald", sans-serif; font-weight: 600; font-size: 26px;
    color: var(--white); text-transform: uppercase; letter-spacing: 1px;
  }
  .service-list {
    position: absolute; top: 560px; left: 0; right: 0; list-style: none;
    font-family: "Oswald", sans-serif; font-weight: 500;
    font-size: 30px; line-height: 44px; text-align: center;
  }
</style>
</head>
<body>
  <section class="card card-front">
    <div class="brand-block">
      <span class="brand-dot"></span>
      <span class="brand-name">Korvane</span>
    </div>
    <h1 class="person-name">Darren Holt</h1>
    <p class="person-role">Owner</p>
    <div class="icon-row">
      <span class="rule"></span>
      <span class="icon-box">
        <svg width="22" height="22" viewBox="0 0 24 24" fill="none" stroke="#fff" stroke-width="2" stroke-linejoin="round"><path d="M5 3h4l2 5-3 2a11 11 0 0 0 6 6l2-3 5 2v4a2 2 0 0 1-2 2A17 17 0 0 1 3 5a2 2 0 0 1 2-2z"/></svg>
      </span>
      <span class="icon-box">
        <svg width="22" height="22" viewBox="0 0 24 24" fill="none" stroke="#fff" stroke-width="2"><rect x="3" y="5" width="18" height="14" rx="1"/><path d="M3 6l9 7 9-7"/></svg>
      </span>
      <span class="icon-box">
        <svg width="22" height="22" viewBox="0 0 24 24" fill="none" stroke="#fff" stroke-width="2"><circle cx="12" cy="12" r="9"/><path d="M3 12h18M12 3c3 3 3 15 0 18M12 3c-3 3-3 15 0 18"/></svg>
      </span>
      <span class="rule"></span>
    </div>
    <div class="contact-list">
      <p>555-014-2287</p>
      <p>korvanedrone@mailbox.com</p>
      <p>www.<span class="web-accent">korvanedrone</span>.com</p>
    </div>
    <div class="divider"></div>
    <address class="address" style="font-style:normal">
      214 W. Orchard St. Brenton<br>OH 45899
    </address>
  </section>

  <section class="card card-back">
    <div class="pattern-field" role="img" aria-label="Repeating pattern of small glossy drone marks across the dark card"></div>
    <span class="back-mark">Korvane</span>
    <ul class="service-list">
      <li>Thermal Image Inspections</li>
      <li>Deer Recovery</li>
      <li>Search &amp; Rescue</li>
      <li>Real Estate Photography</li>
    </ul>
  </section>
</body>
</html>
```